R&T Photography (business cards)

Business cards for a photography business. We also photographs events, portraits, headshots.
Colors: Vanilla w/ dark blue (not Aqua or Navy)
Website: randtphotography482-mailbox.net
Email: randtphotography76@mailbox.net
Company Name: R&T Photography
Letter style/font for company name is French Script
We would like a card that somehow delivers a combination of softness, confidence and strength.

Target Market(s)

Wedding clients

Industry/Entity Type

Business

Font styles to use
Decorative
Script

Colors
0d5ba7
3176b5
5c5c5c
dbdbdb

Requirements
Must have
• Bold and/or raised print for company name. Website should also stand out. Telephone contact numbers are:
• (555) 214-7730
• (555) 862-3046
• Website: RandTPhotohraphy482-mailbox.net
• Business address: PO Box 6204, Orlando, FL 32899
• Back of card should state: referrals are welcome.
Nice to have
• some lace/scroll
Should not have
• Non-metallic.

```html
<!DOCTYPE html>
<html lang="en">
<head>
<meta charset="utf-8">
<title>R&amp;T Photography – Business Cards</title>
<link rel="stylesheet" href="https://fonts.googleapis.com/css2?family=Quintessential&family=Lato:wght@300;400&display=swap">
<style>
  :root {
    --blue: #3176b5;
    --blue-deep: #0d5ba7;
    --grey-text: #5c5c5c;
    --grey-soft: #dbdbdb;
    --paper: #ffffff;
    --edge: #222222;
  }
  * { margin: 0; padding: 0; box-sizing: border-box; }
  html, body {
    width: 1200px;
    height: 934px;
    overflow: hidden;
    background: var(--paper);
  }
  .canvas {
    position: relative;
    width: 1200px;
    height: 934px;
  }
  .card {
    position: absolute;
    top: 90px;
    width: 423px;
    height: 740px;
    background: var(--paper);
    border: 1.5px solid var(--edge);
    overflow: hidden;
  }
  .card--front { left: 88px; }
  .card--back { left: 665px; }

  /* front */
  .logo-lace {
    position: absolute;
    left: 50%;
    top: 56px;
    width: 346px;
    height: 346px;
    margin-left: -173px;
    border-radius: 50%;
    background: radial-gradient(circle, var(--paper) 0 52%, #e6e6e6 53% 62%, var(--grey-soft) 63% 100%);
  }
  .brand {
    position: absolute;
    left: 0;
    right: 0;
    top: 150px;
    text-align: center;
    font-family: "Quintessential", cursive;
    font-weight: 400;
    color: var(--blue);
    line-height: 1;
  }
  .brand__name { display: block; font-size: 84px; }
  .brand__trade { display: block; font-size: 36px; margin-top: 14px; }

  .contact {
    position: absolute;
    left: 0;
    right: 0;
    text-align: center;
    font-family: "Lato", sans-serif;
    font-weight: 300;
    font-size: 21px;
    color: var(--grey-text);
  }
  .contact--phones { top: 468px; word-spacing: 2px; }
  .contact--phones span + span { margin-left: 20px; }
  .contact--web { top: 533px; color: var(--blue); font-weight: 400; }
  .contact--address { top: 599px; }

  .flourish {
    position: absolute;
    left: 46px;
    width: 331px;
    height: 40px;
    border-radius: 20px;
    background: linear-gradient(90deg, rgba(219,219,219,0) 0%, var(--grey-soft) 20%, #e9e9e9 50%, var(--grey-soft) 80%, rgba(219,219,219,0) 100%);
  }
  .card--front .flourish { top: 645px; }

  /* back */
  .lace-band {
    position: absolute;
    left: 0;
    right: 0;
    height: 48px;
    background: linear-gradient(180deg, var(--blue-deep) 0 14%, var(--blue) 15% 100%);
  }
  .lace-band--top { top: 0; }
  .lace-band--bottom { bottom: 0; background: linear-gradient(0deg, var(--blue-deep) 0 14%, var(--blue) 15% 100%); }
  .card--back .flourish--upper { top: 184px; }
  .card--back .flourish--lower { top: 518px; }

  .referral {
    position: absolute;
    left: 0;
    right: 0;
    text-align: center;
    font-family: "Quintessential", cursive;
    color: var(--blue);
    line-height: 1;
  }
  .referral__lead { top: 290px; font-size: 56px; }
  .referral__main { top: 365px; font-size: 90px; }
</style>
</head>
<body>
<main class="canvas">
  <section class="card card--front" aria-label="Front of business card">
    <div class="logo-lace" role="img" aria-label="Circular lace ornament framing the studio name"></div>
    <h1 class="brand">
      <span class="brand__name">R&amp;T</span>
      <span class="brand__trade">photography</span>
    </h1>
    <p class="contact contact--phones"><span>(555) 214-7730</span><span>(555) 862-3046</span></p>
    <p class="contact contact--web">RandTPhotohraphy482-mailbox.net</p>
    <p class="contact contact--address">PO Box 6204, Orlando, FL 32899</p>
    <div class="flourish" role="img" aria-label="Grey scroll flourish divider"></div>
  </section>

  <section class="card card--back" aria-label="Back of business card">
    <div class="lace-band lace-band--top" role="img" aria-label="Blue lace border"></div>
    <div class="flourish flourish--upper" role="img" aria-label="Grey scroll flourish divider"></div>
    <p class="referral referral__lead">referrals are</p>
    <p class="referral referral__main">welcome!</p>
    <div class="flourish flourish--lower" role="img" aria-label="Grey scroll flourish divider"></div>
    <div class="lace-band lace-band--bottom" role="img" aria-label="Blue lace border"></div>
  </section>
</main>
</body>
</html>
```